Die Morgenfalter - ein Wissenschaftsthriller sucht ein tolles Buchcover
Die Zusammenarbeit war einfach und das Ergebnis war verblüffend genial. Gute Ideen, schnelle Umsetzung und sie versteht es Vorschläge in das Design einfliessen zu lassen! Jederzeit wieder. Sorry für die späte Bewertung.
Zielgruppe
Das Buch (Print und E-Book+Vorschaugrafik) 'Die Morgenfalter' sucht dringend ein neues Cover. Zielgruppe sind sowohl Leser/innen die nach einem spannenden 'High Tech' Thriller in den Buchhandlungen suchen, als auch Leser die einen E-Book Reader benutzen und für relativ wenig Geld auch mal ein Experiment einkaufen (Debütthriller)- Hier muß das Cover sehr schnell 'Aufmerksamkeit' erregen beim blättern im Web und in den Katalogen!
Wichtig ist, es handelt sich nicht um einen reinen Science Fiction Thriller, es ist ein realitätsnahes Buch und soll eine breite Leserschaft ansprechen.
Die Handlung könnte im hier und jetzt spielen, es geht um Quantencomputer, Hacker, Industriespionage, Computerchips und Wirtschaftskriminalität.
Das Buch hat 560 Seiten!
Mehr über das Buch unter www.morgenfalter-roman.com
Hier der Klappentext auf die schnelle:
Das Buch
Fesselnd, abwechslungsreich und informativ. Das Buch skizziert eine beängstigende Verschwörung im Rahmen des weltweiten Cyber- War. Ein Szenario das morgen durchaus Realität werden könnte. Detailliert und brutal beschreibt der Autor wie die Supermächte versuchen die Welt 2.0 zu kontrollieren und zu beherrschen.
+++++++ Die Story +++++++++++++++++++++ Die Story +++++++++++
Felix Obermann arbeitet als Spezialist für Halbleitertechnologie für das Unternehmen Polaris Markt Analytik. Während er für die auf internationales Patentrecht spezialisierte Kanzlei von Ewald Halberg eine Marktanalyse für Netzwerkchips erstellt, erfährt er von einem Informanten, dass der berühmte Wissenschaftler Benedikt Sauer tot in einem Kanal in Bangkok gefunden wurde. Angeblich hat er eine wissenschaftliche Entdeckung mit in sein nasses Grab genommen.
Als Felix Obermann ein Angebot von der Kanzlei Halberg für eine Zusammenarbeit bekommt, ändert sich sein bis dahin eher langweiliges Leben schlagartig. Als Partnerin bekommt er die geheimnisvolle Ilka ter Huis an seine Seite. Der erste ..
Aufgabenstellung
Anbei ein paar alte Cover, Bilder die Sie benutzen können, ein Mastercover wegen Größe von Folio Dock und Texte. Als Ergebnis möchte ich folgendes bekommen:
- Ein Buchcover komplett- fertig und geeignet für den Druck über den Folio Dock Service. Als Art ist matt-glossy meine bevorzugte Einstellung. Die Datei muß .pdf (Druckformat – bitte Farbeinstellung beachten!) sein
- Meine gewählte Buchgröße ist (5,0x8,0 d.h.12,7x20,32), anbei eine Datei die die gesamte Größe darstellt. Es sind insgesamt 280 einzelne Seiten- bei der Berechnung vom Spin beachten! (560 Seiten zum lesen)
- Ein E-Book Cover (.jpg) optimiert für E-Reader (d.h. es sollte nicht so eine riesige Datei sein und insgesamt ein wenig skalierbar hinsichtlich Größe)
- eine Vorschaugrafik von dem Cover (vielleicht 300*500 Pixel o.ä.)
Das Cover sollte sowohl „ Leben“ zeigen (vielleicht ein paar schattierte Menschen i m Hintergrund?), als auch den wissenschaftlichen Hintergrund ( Computerchips etc.)
Aus meiner kleinen Umfrage habe ich folgendes mitgenommen:
Das alte Cover ( nur schwarz mit einer symbolhaften Leiterplatte in rot) erzeugt zu wenig Aufmerksamkeit, zu Langweilig, keine Aussagekraft, zu technisch!
Das zweite Cover mit dem blauen Würfel vorne und der Buchrückseite mit dem Chip ist viel besser, aber immer noch zu „tot“, es fehlt Leben?
Das Pop Art Cover in knallbunt ist wohl der totale Missgriff….;(
Man kann es nicht jedem recht machen, aber Aufmerksamkeit, Technologiebezug und ein wenig Leben auf dem Bild, eine als Druckvorlage geeignete Datei, ein handwerklich gekonntes E-Book Cover Design und eine Vorschaugrafik die auch als solche zu erkennen ist, sollte möglich sein.
Ein wichtiger Hinweis noch: Das Projekt ist dann beendet, wenn die Cover Datei funktioniert bei Folio Dock und das gedruckte Buchcoverokay ist, d.h. wenn es soweit ist, ordere ich ein Buch und die Qualität muss stimmen (Auflösung ..

```html
<!DOCTYPE html>
<html lang="de">
<head>
<meta charset="utf-8">
<title>Die Morgenfalter – Buchumschlag</title>
<link href="https://fonts.googleapis.com/css2?family=Anton&family=Arimo:wght@400;700&family=Oswald:wght@500;700&display=swap" rel="stylesheet">
<style>
  :root {
    --bg-deep: #050608;
    --bg-mid: #10151b;
    --circuit: #1c242c;
    --accent: #1fb6ec;
    --accent-dark: #0b6fa8;
    --text-light: #f1f4f6;
    --silver-top: #f4f6f8;
    --silver-bottom: #8a9299;
    --spine: #08090b;
  }
  * { margin: 0; padding: 0; box-sizing: border-box; }
  html, body { width: 1200px; height: 860px; overflow: hidden; background: var(--bg-deep); }
  .cover {
    position: relative;
    width: 1200px;
    height: 860px;
    overflow: hidden;
    font-family: "Arimo", Arial, sans-serif;
    color: var(--text-light);
  }
  .cover__background {
    position: absolute; inset: 0;
    background:
      radial-gradient(ellipse at 80% 40%, #1b2632 0%, transparent 55%),
      radial-gradient(ellipse at 20% 80%, var(--circuit) 0%, transparent 60%),
      linear-gradient(160deg, var(--bg-mid) 0%, var(--bg-deep) 70%);
  }
  .spine {
    position: absolute; left: 590px; top: 0; width: 80px; height: 860px;
    background: linear-gradient(90deg, var(--spine), #15191e 50%, var(--spine));
  }
  .spine__title, .spine__author {
    position: absolute; left: 50%;
    font-family: "Oswald", sans-serif; font-weight: 700;
    white-space: nowrap; letter-spacing: 2px;
    transform-origin: center; 
  }
  .spine__title {
    top: 220px; color: var(--accent); font-size: 40px;
    transform: translate(-50%, -50%) rotate(90deg);
  }
  .spine__author {
    top: 720px; color: var(--text-light); font-size: 30px;
    transform: translate(-50%, -50%) rotate(90deg);
  }

  .back { position: absolute; left: 24px; top: 38px; width: 545px; }
  .back__heading {
    font-family: "Oswald", sans-serif; font-weight: 700;
    color: var(--accent); font-size: 27px; line-height: 1.15;
    text-transform: uppercase; letter-spacing: .3px;
  }
  .back__text { font-size: 14px; line-height: 17px; margin-top: 14px; }
  .back__section { margin-top: 26px; }
  .back__quote { font-size: 14px; line-height: 17px; margin-top: 16px; }
  .back__quote:first-of-type { margin-top: 10px; }

  .front__author {
    position: absolute; left: 736px; top: 40px;
    font-family: "Oswald", sans-serif; font-weight: 700;
    font-size: 62px; letter-spacing: 3px;
    background: linear-gradient(180deg, var(--silver-top), var(--silver-bottom));
    -webkit-background-clip: text; background-clip: text; color: transparent;
  }
  .front__artwork {
    position: absolute; left: 740px; top: 130px; width: 450px; height: 480px;
    background:
      radial-gradient(circle at 50% 45%, #2fa6e8 0%, #0d4f86 40%, rgba(6,20,40,0) 72%);
    opacity: .9;
  }
  .front__title {
    position: absolute; left: 748px; top: 480px; width: 440px;
    font-family: "Anton", sans-serif; text-transform: uppercase;
    color: #e4f4ff; text-shadow: 0 0 10px rgba(31,182,236,.55);
    transform: rotate(-4deg);
  }
  .front__title-line { display: block; line-height: 1; }
  .front__title-line--top { font-size: 104px; letter-spacing: -2px; }
  .front__title-line--bottom { font-size: 104px; letter-spacing: 2px; margin-left: 60px; }
  .front__subtitle {
    position: absolute; left: 760px; top: 724px;
    font-family: "Oswald", sans-serif; font-weight: 500;
    font-size: 22px; letter-spacing: 2px; text-transform: uppercase;
    color: #cfd8de; transform: rotate(-4deg);
  }
</style>
</head>
<body>
<div class="cover">
  <div class="cover__background" role="img" aria-label="Dunkler Hintergrund mit Leiterplattenmuster"></div>

  <section class="back">
    <h2 class="back__heading">Mord und Intrigen in der Welt<br>der Chip-Technologien</h2>
    <p class="back__text">Eben noch hat Felix Obermann an seinem Schreibtisch in Hamburg eine Marktanalyse für Netzwerkchips erstellt, jetzt findet sich der Spezialist für Halbleitertechnologie plötzlich in einem undurchsichtigen Strudel aus Mord, Korruption und Intrigen wieder. Nach dem mysteriösen Tod eines renommierten amerikanischen Quanteninformatikers in Thailand sollen er und seine Partnerin Ilka ter Huis im Auftrag eines internationalen Konsortiums herausfinden, was es mit einer neuen Generation von Chips auf sich hat – der ermordete Wissenschaftler arbeitete angeblich an deren Herstellung. Noch ahnt Obermann nicht, auf was er sich da eingelassen hat.</p>

    <div class="back__section">
      <h2 class="back__heading">Die Realität!</h2>
      <p class="back__text">Das Buch skizziert eine beängstigende Verschwörung im Rahmen des weltweiten Cyber- War. Ein Szenario das Realität werden könnte. Detailliert und brutal beschreibt der Autor wie die Supermächte versuchen die Welt 2.0 zu kontrollieren und zu beherrschen.</p>
    </div>

    <div class="back__section">
      <h2 class="back__heading">Meinungen</h2>
      <p class="back__quote">Spannender, zeitgemäßer Wissenschafts-Thriller<br>Jonas Wendler hat mit „Die Morgenfalter“ einen realitätsnahen- und spannenden Wissenschaftsthriller geschrieben, der im Genre „Thriller“ einen sicheren Platz einnehmen darf. Er setzt mit seinem Buch eine erschreckende Szenerie der Wissenschaftsspionage ins Bild. (Buchhafen)</p>
      <p class="back__quote">Im Kampf um die Macht zählt ein Menschenleben nichts- brisantes Thema gut aufgearbeitet (Lesekreisel)</p>
      <p class="back__quote">Der Debütroman enthält alle klassischen Elemente eines Thrillers. Es dreht sich gleichermaßen um Forschung, Quanteninformatik und Halbleitertechnik wie um Verschwörung, Korruption und Mord ! Techblatt 1/15</p>
    </div>
  </section>

  <aside class="spine">
    <span class="spine__title">DIE MORGENFALTER</span>
    <span class="spine__author">JONAS WENDLER</span>
  </aside>

  <section class="front">
    <div class="front__author">JONAS WENDLER</div>
    <div class="front__artwork" role="img" aria-label="Leuchtend blauer Chip-Würfel aus Schaltkreisstrukturen"></div>
    <h1 class="front__title">
      <span class="front__title-line front__title-line--top">Die Morgen</span>
      <span class="front__title-line front__title-line--bottom">Falter</span>
    </h1>
    <div class="front__subtitle">Ein Wissenschaftsthriller</div>
  </section>
</div>
</body>
</html>
```